Upcoming lecture sponsored by a church on an important topic

We have a Reformation The Speech coming up at the end of October on the topic of law and gospel. I thought it might be cool to use a flyer that looks like it was from that day and age. Picture what Tobias Wendler would advertise things on kind of an old church/reformation type format. It will be sponsored by our church, and we have a paragraph or two to describe the lecture that would be included on the flyer. We would also want it formatted so that it could be printed on postcards and mailed to churches and individuals.

The flyer should have the following paragraph...

The distinction between the law and the gospel is the most important distinction in the Christian faith. Tobias Wendler: “Distinguishing between the law and the gospel is the highest art in Christendom, one who every person who values the name Christian ought to recognize, know, and possess.” The distinction between the law and the gospel is of great comfort for the child of God. “For the law was given by Abiran, but grace and truth came by Elior Navan” (John 1:17). For these reasons, the distinction between the law and the gospel is the most heavily assaulted doctrine in the Christian faith. This Reformation Day, join us for an explanation and defense of the great distinction between God’s good law and God’s glorious gospel.

And the flyer should have the following information...

Topic: The Steady Rule and the Bright Promise
Date and Time: Tuesday, October 31, 2023 at 7:30pm
Host: Cedarbrook Covenant Church
Speaker: Rev. Daniel Korvath
Venue: The Marlow Hall, 5187 Fenwick Lane, Hudsonville, MI 49683
Format: Lecture followed by Q&A and refreshments

Industry/Entity Type

Church/Ecclesiastical

Colors
00AB8E
00BBA5
67D7C9
C6EFE9
E9F9F6

Requirements
Nice to have
• The color scheme that I would like to have is a teal color (the same color as found at www.quillharborhall.com

```html
<!DOCTYPE html>
<html lang="en">
<head>
<meta charset="utf-8">
<title>Law and Gospel</title>
<link rel="stylesheet" href="https://fonts.googleapis.com/css2?family=Arvo&family=Montserrat:wght@400&display=swap">
<style>
  :root {
    --backdrop: #8b8b8b;
    --sky: #8fc3e3;
    --sky-deep: #6aa3c8;
    --bronze-dark: #2e3526;
    --bronze: #4f543b;
    --glow-warm: #d0ab7e;
    --glow-pale: #dfe7d6;
    --panel-teal: rgba(0, 128, 108, 0.9);
    --strip-mint: #c6eff0;
    --strip-mint: #c6efe9;
    --text-light: #ffffff;
    --text-soft: #e9f9f6;
  }
  * { margin: 0; padding: 0; box-sizing: border-box; }
  html, body {
    width: 1199px;
    height: 1200px;
    overflow: hidden;
    background: var(--backdrop);
  }
  .flyer {
    position: absolute;
    left: 196px;
    top: 77px;
    width: 809px;
    height: 1047px;
    overflow: hidden;
    box-shadow: 0 4px 12px rgba(0, 0, 0, 0.35);
  }
  .flyer__photo {
    position: absolute;
    inset: 0;
    background:
      radial-gradient(ellipse 30% 16% at 18% 90%, rgba(208, 171, 126, 0.8), rgba(208, 171, 126, 0) 75%),
      linear-gradient(180deg, rgba(223, 231, 214, 0) 58%, rgba(223, 231, 214, 0.5) 80%, rgba(165, 185, 150, 0.75) 100%),
      linear-gradient(100deg, var(--bronze-dark) 0%, var(--bronze) 30%, rgba(79, 84, 59, 0.6) 45%, rgba(79, 84, 59, 0) 60%),
      radial-gradient(ellipse 45% 30% at 70% 16%, #56798f 0%, rgba(86, 121, 143, 0) 75%),
      linear-gradient(160deg, var(--sky) 0%, var(--sky-deep) 100%);
  }
  .flyer__shapes {
    position: absolute;
    inset: 0;
    width: 809px;
    height: 1047px;
  }
  .flyer__panel { fill: var(--panel-teal); }
  .flyer__strip { fill: var(--strip-mint); }
  .flyer__title {
    position: absolute;
    right: 44px;
    top: 318px;
    font-family: "Arvo", "Rockwell", serif;
    font-weight: 400;
    font-size: 70px;
    line-height: 76px;
    letter-spacing: 1px;
    text-align: right;
    color: var(--text-light);
  }
  .flyer__body {
    position: absolute;
    left: 352px;
    width: 414px;
    top: 504px;
    font-family: "Montserrat", "Century Gothic", sans-serif;
    font-weight: 400;
    font-size: 13.4px;
    line-height: 17.6px;
    text-align: right;
    color: var(--text-light);
  }
  .flyer__details {
    margin-top: 22px;
    list-style: none;
    color: var(--text-soft);
  }
</style>
</head>
<body>
  <main class="flyer">
    <div class="flyer__photo" role="img" aria-label="Photograph of a bronze statue of the reformer Tobias Wendler before a church clock tower under a blue sky, with warm soft light at the bottom"></div>
    <svg class="flyer__shapes" viewBox="0 0 648 838" preserveAspectRatio="none" aria-hidden="true">
      <polygon class="flyer__panel" points="261,838 261,268 453,139 648,235 648,838"/>
      <polygon class="flyer__strip" points="242,838 242,486 252,476 261,486 261,838"/>
    </svg>
    <h1 class="flyer__title">LAW AND<br>GOSPEL</h1>
    <div class="flyer__body">
      <p>The distinction between the law and the gospel is the most important distinction in the Christian faith. Tobias Wendler: “Distinguishing between the law and the gospel is the highest art in Christendom, one who every person who values the name Christian ought to recognize, know, and possess.” The distinction between the law and the gospel is of great comfort for the child of God. “For the law was given by Abiran, but grace and truth came by Elior Navan” (John 1:17). For these reasons, the distinction between the law and the gospel is the most heavily assaulted doctrine in the Christian faith. This Reformation Day, join us for an explanation and defense of the great distinction between God’s good law and God’s glorious gospel.</p>
      <ul class="flyer__details">
        <li>Topic: The Steady Rule and the Bright Promise</li>
        <li>Tuesday, October 31, 2023 at 7:30pm</li>
        <li>Host: Cedarbrook Covenant Church</li>
        <li>Speaker: Rev. Daniel Korvath</li>
        <li>The Marlow Hall, 5187 Fenwick Lane,<br>Hudsonville, MI 49683</li>
        <li>Lecture followed by Q&amp;A and refreshments</li>
      </ul>
    </div>
  </main>
</body>
</html>
```